Business card design needed

Business Card design required for new small plumbing business.
Would like a logo/text look that is simple and unique and does not have to be representative of a plumbing company (ie. having a cartoon plumber or toilet etc) as the companyname is self explanatory.
Would like the main colour to be green (lime green).
Updates

Industry/Entity Type

Plumber

Contact Information for Business Card

BRAVELL PLUMBING
ABN 61 904 127 558 003

Trevor Hasketh
Licensed Plumber 83615
Phone: 0412 870 245

27 Bravell Drive,
Kellmore. 3948 Westvale

Email: bravellplumbing@mailnest.example

Logo Text

Bravell Plumbing

Logo styles of interest
Character Logo
Wordmark Logo
Lettermark Logo

```html
<!DOCTYPE html>
<html lang="en">
<head>
<meta charset="utf-8">
<title>Bravell Plumbing – Business Card</title>
<link rel="stylesheet" href="https://fonts.googleapis.com/css2?family=Cabin:wght@400;500&display=swap">
<style>
  :root {
    --lime: #5bb947;
    --lime-line: #7fcc6c;
    --paper: #f7f7f5;
    --ink: #3a3d3c;
    --ink-soft: #555957;
    --stage: #e9e9e7;
  }
  * { margin: 0; padding: 0; box-sizing: border-box; }
  html, body { width: 1200px; height: 933px; overflow: hidden; }
  body {
    background: var(--stage);
    position: relative;
    font-family: "Cabin", sans-serif;
  }
  .card {
    position: absolute;
    left: 270px;
    width: 660px;
    height: 404px;
    overflow: hidden;
    background: var(--lime);
    box-shadow: 0 6px 18px rgba(0,0,0,.18);
  }
  .card--front { top: 27px; }
  .card--back  { top: 471px; }
  .card__shapes { position: absolute; inset: 0; }

  .business-name {
    position: absolute;
    font-family: "Cabin", sans-serif;
    font-weight: 500;
    color: var(--ink);
    line-height: 1;
    white-space: nowrap;
  }
  .card--front .business-name { right: 34px; top: 58px; font-size: 34px; }
  .card--back .business-name { left: 0; right: 0; top: 178px; font-size: 46px; text-align: center; }

  .contact { position: absolute; left: 26px; top: 240px; color: var(--ink-soft); }
  .contact__name { font-size: 30px; font-weight: 500; color: var(--ink); letter-spacing: .5px; line-height: 1; }
  .contact__first { color: var(--lime); }
  .contact__role { font-size: 15px; margin: 4px 0 12px; color: var(--ink); }
  .contact__list { list-style: none; font-size: 14px; }
  .contact__list li { display: flex; align-items: center; gap: 10px; height: 21px; white-space: nowrap; }
  .icon { width: 15px; height: 15px; flex: none; }
</style>
</head>
<body>

<section class="card card--front" aria-label="Business card front">
  <svg class="card__shapes" viewBox="0 0 660 404" aria-hidden="true">
    <defs>
      <filter id="soft-shadow" x="-10%" y="-10%" width="120%" height="130%">
        <feDropShadow dx="0" dy="3" stdDeviation="4" flood-color="#000" flood-opacity=".22"/>
      </filter>
    </defs>
    <path d="M300 0 C340 70 380 120 470 128 L660 132 L660 0 Z" fill="var(--paper)" filter="url(#soft-shadow)"/>
    <path d="M0 212 C160 198 250 215 300 262 C350 320 390 380 490 404 L0 404 Z" fill="var(--paper)" filter="url(#soft-shadow)"/>
  </svg>

  <p class="business-name">Bravell Plumbing</p>

  <div class="contact">
    <p class="contact__name"><span class="contact__first">trevor</span> hasketh</p>
    <p class="contact__role">licensed plumber 83615</p>
    <ul class="contact__list">
      <li>
        <svg class="icon" viewBox="0 0 16 16" aria-hidden="true"><circle cx="8" cy="8" r="8" fill="var(--ink)"/><path d="M4 8.5 8 4.5 12 8.5V12H4Z" fill="#fff"/></svg>
        27 Bravell Drive, Kellmore 3948 Westvale
      </li>
      <li>
        <svg class="icon" viewBox="0 0 16 16" aria-hidden="true"><circle cx="8" cy="8" r="8" fill="var(--ink)"/><rect x="4.5" y="5" width="7" height="6" rx="1" fill="#fff"/></svg>
        61 904 127 558 003
      </li>
      <li>
        <svg class="icon" viewBox="0 0 16 16" aria-hidden="true"><circle cx="8" cy="8" r="8" fill="var(--ink)"/><path d="M5 4.5c1 0 1.4 2 1 2.6-.3.4.9 2.3 1.6 2.6.6-.4 2.6 0 2.6 1 0 .8-1 1.3-1.8 1.2C6 11.5 4 8 4 6c0-.8.3-1.5 1-1.5Z" fill="#fff"/></svg>
        0412 870 245
      </li>
      <li>
        <svg class="icon" viewBox="0 0 16 16" aria-hidden="true"><circle cx="8" cy="8" r="8" fill="var(--ink)"/><rect x="4" y="5" width="8" height="6" fill="#fff"/><path d="M4 5l4 3.5L12 5" stroke="var(--ink)" stroke-width="1" fill="none"/></svg>
        bravellplumbing@mailnest.example
      </li>
    </ul>
  </div>
</section>

<section class="card card--back" aria-label="Business card back">
  <svg class="card__shapes" viewBox="0 0 660 404" aria-hidden="true">
    <g stroke="var(--lime-line)" stroke-width="3" opacity=".7">
      <line x1="0" y1="18" x2="660" y2="18"/>
      <line x1="0" y1="34" x2="660" y2="34"/>
      <line x1="0" y1="300" x2="660" y2="300"/>
      <line x1="0" y1="316" x2="660" y2="316"/>
      <line x1="0" y1="332" x2="660" y2="332"/>
      <line x1="0" y1="348" x2="660" y2="348"/>
    </g>
  </svg>
  <p class="business-name">Bravell Plumbing</p>
</section>

</body>
</html>
```